zPivotra EMV Integration Platform

Design Goal:
Create a professional/technology based one page design that conveys our value proposition for Point of Sale systems to remove the need to ever do a payment integration again. zPivotra provides a single point of access to credit card machines globally with an easy web based API.

Design look and feel:
Professional and tech driven design that communicates the single point of integration for EMV payments globally.

Images/ICONs:
All images and ICONs should address our clients, all of our clients are point of sale companies, software companies or larger merchants. Our clients are www.talvorix.com, http://quandersoft.com/, www.harrowpinecommerce.com and other similar.
Updates

Please don't use our existing design and attempt to make it better. We're looking for a new look and design, take a look at the two examples I provided. One is really good, simple to design and unique. User real images to help improve the design

Target Market(s)

Point of Sale systems, software companies, any retail solution looking to accept credit cards via EMV payment terminals

Industry/Entity Type

Business Software

Number of Pages Required

1 page

Font styles to use
Sans Serif

Requirements
Must have
• Very professional, unique and simple with different look. Read the PDF to see the sections that need to be broken out.
Nice to have
• Looking for unique design, similar to BUT not the same as
• http://www.belthacore.com/
• https://zelvo.com/
Should not have
• Should not use non-images pictures, all pictures and look should be professional and address high end software companies. Don't copy our existing and put in a couple new images

```html
<!DOCTYPE html>
<html lang="en">
<head>
<meta charset="utf-8">
<title>zPivotra – Gateway to Global Payment Terminals</title>
<link href="https://fonts.googleapis.com/css2?family=Roboto:ital,wght@0,300;0,400;0,500;0,700;1,300&display=swap" rel="stylesheet">
<style>
:root{
  --green:#7cc242;
  --navy:#2b4576;
  --navy-dark:#223a66;
  --ink:#333a44;
  --muted:#8a9099;
  --line:#e3e5e8;
  --soft:#f4f5f6;
  --white:#ffffff;
}
*{box-sizing:border-box;margin:0;padding:0}
html,body{width:1200px;height:4348px;overflow:hidden}
body{position:relative;font-family:'Roboto',sans-serif;color:var(--ink);background:var(--white)}
section,header,footer{position:absolute;left:0;width:1200px}
.center{text-align:center}
.eyebrow{font-size:13px;color:var(--muted);text-align:center}
.section-title{font-size:27px;font-weight:300;text-align:center;color:var(--ink)}
.section-title b{font-weight:700}

/* hero */
.hero{top:0;height:522px;background:linear-gradient(160deg,#5d5f5c 0%,#3c3f3d 45%,#2a2c2b 100%);color:var(--white)}
.hero-photo{position:absolute;inset:0;background:radial-gradient(ellipse at 30% 70%,rgba(150,140,120,.45),transparent 60%),radial-gradient(ellipse at 80% 60%,rgba(120,115,100,.35),transparent 55%)}
.nav{position:absolute;top:24px;left:80px;right:80px;height:36px;display:flex;align-items:center}
.brand{font-size:26px;font-weight:500;letter-spacing:-.5px}
.brand small{display:block;font-size:8px;letter-spacing:1.5px;color:#cfd2cf;font-weight:400;margin-top:-2px}
.nav-links{display:flex;gap:22px;margin-left:70px;font-size:12px;font-weight:500}
.nav-phone{margin-left:auto;border:1px solid var(--green);color:var(--green);font-size:12px;padding:8px 14px}
.nav-quote{margin-left:12px;border:1px solid var(--green);color:var(--green);font-size:12px;padding:8px 12px}
.hero h1{position:absolute;top:146px;width:100%;text-align:center;font-size:30px;font-weight:300}
.hero h1 b{font-weight:700}
.hero p{position:absolute;top:196px;left:320px;width:560px;text-align:center;font-size:15px;line-height:20px;color:#e6e7e5}
.btn-hero{position:absolute;top:268px;left:522px;width:156px;height:36px;border:1px solid var(--white);background:rgba(0,0,0,.35);font-size:13px;line-height:34px;text-align:center}
.hero-chev{position:absolute;top:380px;left:591px}
.hero-foot{position:absolute;top:442px;width:100%;text-align:center;font-size:12px;color:#d8d9d7}

/* features */
.features{top:522px;height:353px}
.feature{position:absolute;top:62px;width:286px;height:228px;border:1px solid var(--line);background:var(--white);text-align:center;padding:44px 30px 0}
.feature.raised{top:56px;box-shadow:0 6px 22px rgba(0,0,0,.13);border-color:transparent}
.feature h3{font-size:15px;font-weight:700;margin-top:14px}
.feature p{font-size:12px;line-height:16px;color:var(--muted);margin-top:8px}

/* pos */
.pos{top:875px;height:487px;background:linear-gradient(180deg,#f3f3f2 0%,#ecebea 60%,#d8c9b3 78%,#c9b497 100%)}
.pos h2{position:absolute;top:62px;width:100%;text-align:center;font-size:25px;font-weight:300}
.pos h2 b{font-weight:700}
.pos p{position:absolute;top:100px;left:330px;width:540px;text-align:center;font-size:12px;line-height:16px;color:#555}
.pos-devices{position:absolute;top:150px;left:280px;width:640px;height:300px;background:linear-gradient(180deg,rgba(210,210,212,.7),rgba(150,150,155,.55));border-radius:6px}

/* countries */
.countries{top:1362px;height:705px}
.world-map{position:absolute;top:148px;left:300px;width:620px;height:340px;border-radius:8px;background:linear-gradient(135deg,#d6e6f3 0%,#bcd5ea 55%,#d9e8f4 100%)}
.map-tag{position:absolute;top:162px;left:526px;background:var(--navy);color:var(--white);font-size:11px;padding:5px 10px;border-radius:12px}
.divider{position:absolute;left:155px;width:890px;height:1px;background:var(--line)}
.clients-label{position:absolute;top:520px;left:570px;width:60px;background:var(--white);text-align:center;font-size:12px;color:var(--muted)}
.client-row{position:absolute;top:600px;left:150px;width:900px;display:flex;justify-content:space-between;align-items:center}
.client{font-size:22px;color:#8e9298;font-weight:400;width:150px;text-align:center}

/* commands */
.commands{top:2067px;height:397px;background:var(--soft)}
.tabs{position:absolute;left:418px;display:flex;font-size:12px}
.tab{width:182px;height:30px;line-height:30px;text-align:center;background:var(--white);border:1px solid var(--line);color:var(--muted)}
.tab.active{background:var(--green);border-color:var(--green);color:var(--white)}
.command-box{position:absolute;top:194px;left:155px;width:890px;height:170px;background:var(--white);text-align:center}
.command-box h4{font-size:14px;font-weight:500;margin-top:22px}
.command-box code{display:block;font-family:'Roboto',sans-serif;font-style:italic;font-weight:300;font-size:13px;color:#666;margin:14px auto 0;width:620px;line-height:18px;word-break:break-all}
.dots{position:absolute;bottom:24px;left:0;width:100%;display:flex;justify-content:center;gap:7px}
.dots i{width:6px;height:6px;border-radius:50%;background:#d0d3d7}
.dots i.on{background:var(--green)}
.arrow{position:absolute;width:30px;height:30px;border-radius:50%;display:flex;align-items:center;justify-content:center}
.arrow.light{background:#e6e8eb}
.arrow.dark{background:var(--navy)}
.arrow.white{background:var(--white)}

/* partners */
.partners{top:2464px;height:421px}
.partner-band{position:absolute;top:102px;left:0;width:1200px;height:320px}
.partner-photo{position:absolute;left:0;top:0;width:524px;height:320px;background:linear-gradient(120deg,#9aa1a6 0%,#6f777d 50%,#4a5157 100%)}
.partner-info{position:absolute;left:524px;top:0;width:676px;height:320px;background:var(--navy);color:var(--white)}
.partner-logo{position:absolute;left:-65px;top:95px;width:124px;height:124px;border-radius:50%;background:var(--white);color:var(--navy);font-size:18px;font-weight:500;text-align:center;line-height:124px}
.partner-info h3{position:absolute;left:88px;top:82px;font-size:19px;font-weight:700}
.partner-info p{position:absolute;left:88px;top:114px;width:420px;font-size:12px;line-height:16px;color:#dbe2ee}

/* pricing */
.pricing{top:2885px;height:782px}
.plan{position:absolute;top:211px;width:272px;height:383px;background:var(--white);box-shadow:0 2px 14px rgba(0,0,0,.09);text-align:center}
.plan h4{font-size:14px;font-weight:500;margin-top:22px}
.plan .per{font-size:12px;color:var(--muted);margin-top:2px}
.price-band{position:absolute;top:64px;left:0;width:272px;height:76px}
.price{position:absolute;top:76px;left:101px;width:70px;height:70px;border-radius:50%;background:var(--navy);color:var(--white);font-size:30px;font-weight:500;line-height:70px}
.price.green{background:var(--green)}
.price sup{font-size:12px;vertical-align:top;position:relative;top:-8px}
.plan ul{list-style:none;position:absolute;top:170px;left:20px;width:232px;font-size:12px;color:var(--muted)}
.plan li{height:35px;line-height:35px;border-bottom:1px solid #f0f1f2}
.plan li.dark{color:var(--ink)}
.plan li:last-child{border-bottom:0}
.btn-plan{position:absolute;top:331px;left:76px;width:120px;height:30px;line-height:28px;font-size:12px;border:1px solid var(--green);color:var(--green)}
.btn-plan.solid{background:var(--green);color:var(--white)}
.custom{position:absolute;top:658px;width:100%;text-align:center;font-size:19px;font-weight:300}
.custom b{font-weight:700}

/* inquiry */
.inquiry{top:3667px;height:609px;background:var(--navy);color:var(--white)}
.contact-col{position:absolute;top:82px;width:240px;text-align:center;font-size:12px;line-height:17px;color:#dbe2ee}
.contact-col .phone{color:var(--green);font-size:19px;line-height:24px;letter-spacing:1px}
.contact-col a{color:var(--white);text-decoration:underline}
.form-title{position:absolute;top:226px;left:0;width:100%;text-align:center;font-size:23px;font-weight:300}
.form-rule{position:absolute;top:241px;height:1px;background:rgba(255,255,255,.35)}
.field{position:absolute;height:30px;background:var(--white);font-size:11px;color:#a8adb5;padding:9px 10px}
.btn-send{position:absolute;top:4189px;left:510px;width:180px;height:34px;border:1px solid var(--white);background:var(--navy);color:var(--white);font-size:12px;line-height:32px;text-align:center}

/* bottom bar */
.bottom{top:4276px;height:72px;background:var(--white);display:flex;align-items:center;padding:0 155px;font-size:12px;color:var(--muted)}
.socials{margin-left:auto;display:flex;gap:10px}
.socials i{width:26px;height:26px;border-radius:50%;border:1px solid var(--green)}
.socials i.fill{background:var(--green)}
.socials i.top{background:var(--navy);border-color:var(--navy);display:flex;align-items:center;justify-content:center}
</style>
</head>
<body>

<header class="hero">
  <div class="hero-photo" role="img" aria-label="Photo of a hand tapping a card on a payment terminal at a shop counter"></div>
  <nav class="nav">
    <div class="brand">zPivotra<small>CONNECTING TERMINALS</small></div>
    <div class="nav-links"><span>Cloud Based</span><span>Payment Terminals</span><span>Countries</span><span>Integration</span><span>Partners</span><span>Pricing</span><span>Contact Us</span></div>
    <div class="nav-phone">&#9742; 1-800-555-0147</div>
    <div class="nav-quote">Get A Quote</div>
  </nav>
  <h1>Gateway to Global <b>Payment Terminals</b></h1>
  <p>Bring the power and capabilities of every Credit Card Terminal to your software, Point of Sale System, or Business Management Application with ease.</p>
  <div class="btn-hero">Get Started Now</div>
  <svg class="hero-chev" width="18" height="12" viewBox="0 0 18 12"><path d="M2 2l7 7 7-7" fill="none" stroke="#7cc242" stroke-width="2"/></svg>
  <div class="hero-foot">Features</div>
</header>

<section class="features">
  <div class="feature" style="left:154px">
    <svg width="46" height="46" viewBox="0 0 46 46"><circle cx="23" cy="23" r="21" fill="#7cc242"/><path d="M10 17c6-2 9 3 13 1s4-7 9-6M9 28c5 0 8 4 13 2M26 32c3-3 8-2 11-5" stroke="#fff" stroke-width="3" fill="none"/></svg>
    <h3>Single Global Integration</h3>
    <p>Accepts EMV, tap wallets, phone wallets, debit cards, Credit Cards, Debit cards and host of other payments globally.</p>
  </div>
  <div class="feature raised" style="left:452px">
    <svg width="50" height="46" viewBox="0 0 50 46"><path d="M13 36a10 10 0 0 1 1-20 13 13 0 0 1 25 3 8.5 8.5 0 0 1-1 17z" fill="#7cc242"/><path d="M25 33V22m-5 5l5-5 5 5" stroke="#fff" stroke-width="3" fill="none"/></svg>
    <h3>Cloud Based</h3>
    <p>Use your POS system with any POS device, with any browser, you leverage payments from the Cloud.</p>
  </div>
  <div class="feature" style="left:758px">
    <svg width="46" height="46" viewBox="0 0 46 46"><rect x="11" y="11" width="24" height="24" fill="none" stroke="#7cc242" stroke-width="3"/><rect x="17" y="17" width="12" height="12" fill="#7cc242"/><path d="M17 4v7M23 4v7M29 4v7M17 35v7M23 35v7M29 35v7M4 17h7M4 23h7M4 29h7M35 17h7M35 23h7M35 29h7" stroke="#7cc242" stroke-width="2.5"/></svg>
    <h3>Processor Agnostic</h3>
    <p>Use the processor of your choice with the freedom, security and capabilities of dozens of Credit Card Devices.</p>
  </div>
</section>

<section class="pos">
  <h2>Any PC, Tablet, Slate, Laptop - <b>No Software</b></h2>
  <p>zPivotra provides the unique ability to use dozens of POS Payment Devices with your preferred Point of Sale system in the cloud. No software installs.</p>
  <div class="pos-devices" role="img" aria-label="Point of sale hardware on a wooden counter: card terminal, receipt printers, cash drawer with touchscreen and scanner"></div>
</section>

<section class="countries">
  <div class="eyebrow" style="position:absolute;top:60px;width:100%">Countries</div>
  <h2 class="section-title" style="position:absolute;top:78px;width:100%">We Control <b>Terminals</b></h2>
  <div class="world-map" role="img" aria-label="World map with location markers for supported countries"></div>
  <div class="map-tag">United Kingdom</div>
  <div class="divider" style="top:528px"></div>
  <div class="clients-label">Clients</div>
  <div class="client-row">
    <span class="client">Brindlo</span><span class="client">Molarix</span><span class="client">Quiksel</span><span class="client">Talvorix</span><span class="client">Medatrin</span>
  </div>
</section>

<section class="commands">
  <div class="eyebrow" style="position:absolute;top:82px;width:100%">Easy to Integrate</div>
  <h2 class="section-title" style="position:absolute;top:100px;width:100%">Standard <b>Commands</b></h2>
  <div class="tabs" style="top:153px"><div class="tab active">Standard Commands</div><div class="tab">Gift Card Examples</div></div>
  <div class="command-box">
    <h4>Void Command</h4>
    <code>https://zpivotraapp.com/terminal.aspx?cmd=void&amp;APIKey={key}&amp;APIPassword={pwd}&amp;Amount=200&amp;terminalId={id}&amp;refId={ref}</code>
    <div class="dots"><i></i><i></i><i class="on"></i><i></i><i></i><i></i></div>
  </div>
  <div class="arrow light" style="left:90px;top:264px"><svg width="10" height="10" viewBox="0 0 10 10"><path d="M7 1L3 5l4 4" stroke="#888" stroke-width="1.6" fill="none"/></svg></div>
  <div class="arrow dark" style="left:1080px;top:264px"><svg width="10" height="10" viewBox="0 0 10 10"><path d="M3 1l4 4-4 4" stroke="#fff" stroke-width="1.6" fill="none"/></svg></div>
</section>

<section class="partners">
  <div class="eyebrow" style="position:absolute;top:22px;width:100%">Provides zPivotra at No Cost</div>
  <h2 class="section-title" style="position:absolute;top:42px;width:100%">Processing <b>Partners</b></h2>
  <div class="partner-band">
    <div class="partner-photo" role="img" aria-label="Photo of a card being inserted into a countertop payment terminal"></div>
    <div class="partner-info">
      <div class="partner-logo">Termvance</div>
      <h3>Card Terminals We Control</h3>
      <p>Payvelo Systems is a unique card payment device organization that sees beyond standard payments. With solutions such as their Call Me support, Card Loyalty, Pay at Table, and flexible application firmware, zPivotra and Payvelo address gaps in the market for ease, speed and unlimited abilities within the credit card device. Payvelo and zPivotra have an aggressive road map combining the offline and retail market without complexities and ease of use.</p>
    </div>
    <div class="arrow white" style="left:90px;top:145px"><svg width="10" height="10" viewBox="0 0 10 10"><path d="M7 1L3 5l4 4" stroke="#888" stroke-width="1.6" fill="none"/></svg></div>
    <div class="arrow white" style="left:1080px;top:145px"><svg width="10" height="10" viewBox="0 0 10 10"><path d="M3 1l4 4-4 4" stroke="#2b4576" stroke-width="1.6" fill="none"/></svg></div>
  </div>
</section>

<section class="pricing">
  <div class="eyebrow" style="position:absolute;top:70px;width:100%">Credit Card Terminal</div>
  <h2 class="section-title" style="position:absolute;top:90px;width:100%">Pricing <b>Plans</b></h2>
  <div class="tabs" style="top:150px;left:424px"><div class="tab active" style="width:176px">Existing Merchant</div><div class="tab" style="width:176px">New Merchant</div></div>

  <div class="plan" style="left:160px">
    <h4>Individual</h4><div class="per">(Per Terminal Per Month)</div>
    <svg class="price-band" viewBox="0 0 272 76"><path d="M0 0h272v44L136 76 0 44z" fill="#f6f7f8"/></svg>
    <div class="price"><sup>$</sup>9</div>
    <ul><li>–</li><li>11.9% per transaction</li><li class="dark">1 free card reader</li><li>Unlimited US based support</li></ul>
    <div class="btn-plan">Select Plan</div>
  </div>
  <div class="plan" style="left:464px">
    <h4>Professional</h4><div class="per">(Per Month)</div>
    <svg class="price-band" viewBox="0 0 272 76"><path d="M0 0h272v44L136 76 0 44z" fill="#f6f7f8"/></svg>
    <div class="price green"><sup>$</sup>79</div>
    <ul><li>Includes 10 terminals</li><li>0.0% per transaction</li><li class="dark">1 free card reader</li><li>Unlimited US based support</li></ul>
    <div class="btn-plan solid">Select Plan</div>
  </div>
  <div class="plan" style="left:768px">
    <h4>Business</h4><div class="per">(Per Month)</div>
    <svg class="price-band" viewBox="0 0 272 76"><path d="M0 0h272v44L136 76 0 44z" fill="#f6f7f8"/></svg>
    <div class="price"><sup>$</sup>299</div>
    <ul><li>Includes 25 terminals</li><li>No per transaction Fee</li><li class="dark">2 free card reader</li><li>Unlimited US based support</li></ul>
    <div class="btn-plan">Select Plan</div>
  </div>

  <div class="custom">Need More Terminals or Would Like a Custom Quote? <b>Contact Us</b></div>
  <svg style="position:absolute;top:718px;left:594px" width="12" height="8" viewBox="0 0 12 8"><path d="M1 1l5 5 5-5" stroke="#9aa0a8" stroke-width="1.5" fill="none"/></svg>
</section>

<section class="inquiry">
  <div class="contact-col" style="left:230px">
    <svg width="14" height="18" viewBox="0 0 14 18"><path d="M7 17s6-7 6-10A6 6 0 0 0 1 7c0 3 6 10 6 10z" fill="#fff"/><circle cx="7" cy="7" r="2.2" fill="#2b4576"/></svg>
    <div style="margin-top:14px">240 Larkfield Street, Northmere<br>Alderton, ST 00418</div>
  </div>
  <div class="contact-col" style="left:480px">
    <svg width="16" height="16" viewBox="0 0 16 16"><path d="M3 1l3 3-2 2c1 2 3 4 6 6l2-2 3 3-2 2C7 15 1 9 1 3z" fill="#7cc242"/></svg>
    <div class="phone" style="margin-top:10px">1 - 800 - 555 - 0147</div>
    <div style="color:#7cc242">support@talvorix.com</div>
  </div>
  <div class="contact-col" style="left:730px">
    <div style="font-size:18px;font-weight:700;color:#fff">?</div>
    <div style="margin-top:10px">Have a Question?<br><a>FAQs</a></div>
  </div>
  <div class="form-rule" style="left:155px;width:340px"></div>
  <div class="form-title">Send Your Inquirie</div>
  <div class="form-rule" style="left:705px;width:340px"></div>
</section>

<div class="field" style="top:3957px;left:310px;width:282px">Name</div>
<div class="field" style="top:3957px;left:615px;width:278px">Email</div>
<div class="field" style="top:4003px;left:310px;width:282px">Phone</div>
<div class="field" style="top:4003px;left:615px;width:278px">Select Your Country &#9662;</div>
<div class="field" style="top:4048px;left:310px;width:583px;height:98px">Message</div>
<div class="btn-send">&#10148; Send Your Inquirie</div>

<footer class="bottom">
  <span>© 2016 zPivotra. All rights reserved. &nbsp;•&nbsp; Privacy &amp; Terms &nbsp;•&nbsp; Blog</span>
  <div class="socials">
    <i></i><i class="fill"></i><i></i><i></i>
    <i class="top"><svg width="10" height="8" viewBox="0 0 10 8"><path d="M1 6l4-4 4 4" stroke="#fff" stroke-width="1.6" fill="none"/></svg></i>
  </div>
</footer>

</body>
</html>
```